The first and only organic certified snacks manufacturer in Singapore (Meridel Provisions)needs a pac

We are a Singapore based certified organic snacks manufacturer and raw foods importing company. We deal with a variety of organic products and have been in the Singapore’s food industry for some time now. We are looking for a new packaging design for our product line CALVORA- Plain.
Design requirements:
1.We want a 10x10 cm label design that can be printed at the front and back of a stand-up pouch.
2. We need a design for around 15 different products that are uniform and can be extended easily to cover 30-40 products in future.
3. The stand-up pouch that we will be using is transparent, two sizes (12 x 6 x 21 cm and 16 x 8 x 23 cm), and the label is 10x10 cm
4. We don't have a brand logo and are currently using the word Calvora as the logo, the font is Glacial Indifference.
5.We need a design that is contemporary, clean and simple and using different colour combinations except green and brown(overused by organic competitors)
6.One label/print on each front and back, ca 10x10 cm.
Essential information:
Contents:
1.Filling weight
2.Product nameï‚§
3.Brand name and/or logo (yet to be designed)
4.Originï‚§
5.EU/USDA/HALAL logosï‚§
6.MDP (meridel provisions) logo
7.Expiration date

7.The original file should be in the .ai (Adobe Illustrator) format.
Please find attached the certification logos, fonts and the current CALVORA-Plain .ai files
Updates

Target Market(s)

everyone who likes to eat and use healthy products

Industry/Entity Type

Food Production

Font styles to use
Other font styles liked:
• Glacial Indiffrence

Colors
fbf063
00a990
85cae6
3377b5
876aae
b768aa
e667a6
f04a50
ffc214

Requirements
Must have
• contemporary clean designs. use of different patterns is suggested
Nice to have
Should not have
• too much use of green, orange and brown colour. pictures of food products.

```html
<!DOCTYPE html>
<html lang="en">
<head>
<meta charset="utf-8">
<title>Calvora Plain – Organic Roasted Hazelnuts Label</title>
<link rel="stylesheet" href="https://fonts.googleapis.com/css2?family=Jost:wght@600&family=Oswald:wght@500;600&family=Dancing+Script:wght@600&display=swap">
<style>
  :root {
    --page: #ffffff;
    --label: #ffffff;
    --frame: #85cae6;
    --brand: #3377b5;
    --brand-square: #876aae;
    --product: #6a4f94;
    --ribbon: #f04a50;
    --accent-pink: #b768aa;
    --accent-rose: #e667a6;
    --rule: #85cae6;
    --badge: #8a8a9a;
    --art-light: #fffbe0;
    --art-mid: #fbf063;
    --art-edge: #e6a6cf;
    --ink: #333344;
  }
  html, body {
    margin: 0;
    padding: 0;
    width: 1200px;
    height: 1200px;
    overflow: hidden;
    background: var(--page);
  }
  .label {
    position: absolute;
    left: 40px;
    top: 40px;
    width: 1120px;
    height: 1120px;
    background: var(--label);
    box-shadow: 0 0 0 1px #eeeeee;
  }
  .pattern-field {
    position: absolute;
    left: 38px; top: 38px; right: 38px; bottom: 38px;
    border-radius: 24px;
    background: radial-gradient(circle at 50% 45%, #ffffff 0%, #f3f5f8 100%);
  }
  .label-frame {
    position: absolute;
    left: 34px; top: 34px; right: 34px; bottom: 34px;
    border: 4px solid var(--frame);
    border-radius: 26px;
  }
  .brand {
    position: absolute;
    left: 0;
    width: 100%;
    top: 62px;
    display: flex;
    flex-direction: column;
    align-items: center;
    font-family: "Jost", sans-serif;
    font-weight: 600;
    color: var(--brand);
    font-size: 150px;
    line-height: 150px;
    letter-spacing: 2px;
  }
  .brand-line { display: flex; align-items: center; gap: 36px; }
  .brand-mark {
    width: 110px;
    height: 100px;
    background: var(--brand-square);
  }
  .hero-art {
    position: absolute;
    left: 320px;
    top: 400px;
    width: 480px;
    height: 420px;
    border-radius: 50%;
    background: radial-gradient(circle, var(--art-light) 0%, var(--art-mid) 60%, var(--art-edge) 100%);
    opacity: 0.8;
  }
  .tagline {
    position: absolute;
    left: 0; width: 100%;
    top: 462px;
    margin: 0;
    text-align: center;
    font-family: "Oswald", sans-serif;
    font-weight: 600;
    color: var(--ribbon);
    font-size: 32px;
    line-height: 40px;
    letter-spacing: 6px;
  }
  .tagline-script {
    position: absolute;
    left: 0; width: 100%;
    top: 508px;
    margin: 0;
    text-align: center;
    font-family: "Dancing Script", cursive;
    font-weight: 600;
    color: var(--accent-pink);
    font-size: 36px;
    line-height: 44px;
  }
  .product-band {
    position: absolute;
    left: 150px;
    width: 820px;
    top: 600px;
    height: 110px;
    border-top: 3px solid var(--rule);
    border-bottom: 3px solid var(--rule);
    background: rgba(255,255,255,0.9);
    display: flex;
    align-items: center;
    justify-content: center;
  }
  .product-name {
    margin: 0;
    font-family: "Oswald", sans-serif;
    font-weight: 600;
    color: var(--product);
    font-size: 60px;
    line-height: 70px;
    white-space: nowrap;
  }
  .weight-ribbon {
    position: absolute;
    left: 470px;
    top: 728px;
    width: 180px;
    height: 84px;
    background: var(--ribbon);
    border-radius: 10px;
    color: #ffffff;
    text-align: center;
    font-family: "Oswald", sans-serif;
  }
  .weight-ribbon .weight {
    display: block;
    font-size: 36px;
    font-weight: 600;
    line-height: 50px;
  }
  .weight-ribbon .badge-text {
    display: block;
    font-size: 18px;
    letter-spacing: 3px;
    line-height: 24px;
  }
  .claims {
    position: absolute;
    left: 0; width: 100%;
    top: 842px;
    margin: 0;
    text-align: center;
    font-family: "Oswald", sans-serif;
    font-weight: 500;
    color: var(--accent-pink);
    font-size: 44px;
    line-height: 56px;
    letter-spacing: 1px;
  }
  .info-row {
    position: absolute;
    left: 96px;
    right: 96px;
    top: 916px;
    height: 44px;
    display: flex;
    align-items: center;
    justify-content: space-between;
    font-family: "Oswald", sans-serif;
    font-weight: 500;
    font-size: 26px;
    color: var(--ink);
  }
  .origin span { color: var(--brand); }
  .maker { display: flex; align-items: center; gap: 12px; color: var(--product); }
  .maker-square { width: 26px; height: 26px; background: var(--accent-rose); }
  .cert-row {
    position: absolute;
    left: 96px;
    right: 96px;
    top: 986px;
    height: 60px;
    display: flex;
    align-items: center;
    justify-content: space-between;
  }
  .cert { border: 3px solid var(--badge); background: #ffffff; box-sizing: border-box; }
  .cert-oval { width: 80px; height: 50px; border-radius: 50%; }
  .cert-rect { width: 96px; height: 50px; border-radius: 4px; }
  .cert-square { width: 50px; height: 50px; border-radius: 4px; }
  .cert-circle { width: 54px; height: 54px; border-radius: 50%; }
  .cert-flag { width: 84px; height: 56px; border: none; background: var(--frame); }
  .exp-box {
    width: 180px;
    height: 50px;
    border: 3px solid var(--badge);
    font-family: "Oswald", sans-serif;
    font-size: 20px;
    color: var(--ink);
    padding: 6px 8px;
    box-sizing: border-box;
  }
</style>
</head>
<body>
  <main class="label">
    <div class="pattern-field" role="img" aria-label="Faint repeating pattern of whole nuts in light grey"></div>
    <div class="label-frame"></div>

    <div class="brand">
      <div class="brand-line">CALVORA</div>
      <div class="brand-line">PLAIN<div class="brand-mark"></div></div>
    </div>

    <div class="hero-art" role="img" aria-label="Illustrated wreath of mixed nuts with leaves"></div>
    <p class="tagline">100% NATURAL</p>
    <p class="tagline-script">and healthful</p>

    <div class="product-band">
      <h1 class="product-name">ORGANIC ROASTED HAZELNUTS</h1>
    </div>

    <div class="weight-ribbon">
      <span class="weight">℮ 250g</span>
      <span class="badge-text">BEST CHOICE</span>
    </div>

    <p class="claims">RELAXATION • HEALTH • ENDURANCE</p>

    <div class="info-row">
      <div class="origin">Origin: <span>Turkey</span></div>
      <div class="maker"><div class="maker-square"></div>Meridel Provisions</div>
    </div>

    <div class="cert-row">
      <div class="cert cert-oval"></div>
      <div class="cert cert-rect"></div>
      <div class="cert cert-square"></div>
      <div class="cert cert-square"></div>
      <div class="exp-box">Exp. Date:</div>
      <div class="cert cert-circle"></div>
      <div class="cert cert-circle"></div>
      <div class="cert cert-flag"></div>
    </div>
  </main>
</body>
</html>
```